Business Card Design

We like to use greens as you will see in our logo (but not TOO much green). We are a Dental Clinic in a somewhat eccentric community. We do not like the dated sharp designs which we see many dentists use. We're looking for something bright and fresh while still maintaining the integrity of the profession. Elegance is not necessarily what we are going for... we need for the design to be "mature" but also up-lifting.

See our logo.
Updates

Project Deadline Extended
Reason: We have 5 designs which we like. But we'd like to see a few more before committing to a design.

Project Deadline Extended
Reason: We are awaiting revisions to this project. We are still welcoming designs while we wait to see if designers are able to provide to us the revisions we require in order to proceed with a selection.

Target Market(s)

Younger families - ages late 20's to early 40's

Industry/Entity Type

Business

Contact Information for Business Card

Marlow T. Venn DDS 2737 S. Fennimore Ave. Ste. 8 Royal Oak, MI 48059 (248)555-0174 FX (248)555-0189 info@BrightwaveDentalMi.example BrigthwaveDentalMi.example on the back of the card we need an appointment reminder (For____ Date___ Time____) with "If you are unable to keep your appointment, kindly give 48 hours notice" at the bottom. No use of teeth in the design. DOUBLE SIDED DESIGN

Requirements
Should not have
• The use of pictures of teeth

```html
<!DOCTYPE html>
<html lang="en">
<head>
<meta charset="utf-8">
<title>Brightwave Dental Care – Business Card</title>
<link rel="stylesheet" href="https://fonts.googleapis.com/css2?family=Arimo:ital,wght@1,700&family=Open+Sans:wght@400;600&display=swap">
<style>
  :root {
    --leaf: #8dc63f;
    --forest: #3d7f3a;
    --paper: #ffffff;
    --backdrop: #e6e8e3;
    --card-w: 840px;
    --card-h: 480px;
  }
  * { box-sizing: border-box; margin: 0; padding: 0; }
  html, body {
    width: 1200px; height: 1200px; overflow: hidden;
    background: var(--backdrop);
  }
  .sheet {
    width: 1200px; height: 1200px;
    display: flex; flex-direction: column; align-items: center;
    justify-content: center; gap: 80px;
  }
  .card {
    position: relative;
    width: var(--card-w); height: var(--card-h);
    overflow: hidden;
    box-shadow: 0 6px 18px rgba(0,0,0,.15);
  }

  /* Appointment side */
  .appointment { background: var(--leaf); font-family: "Arimo", Arial, sans-serif; }
  .appointment__fields {
    position: absolute; left: 70px; top: 150px; width: 560px;
    display: flex; flex-direction: column; gap: 22px;
  }
  .appointment__rule {
    border-bottom: 2px dotted var(--paper); height: 0; margin-left: 80px;
  }
  .appointment__field { display: flex; align-items: flex-end; gap: 14px; }
  .appointment__label {
    width: 66px; color: var(--paper); font-style: italic; font-weight: 700;
    font-size: 22px; letter-spacing: .5px;
  }
  .appointment__line { flex: 1; border-bottom: 2px dotted var(--paper); margin-bottom: 6px; }
  .appointment__notice {
    position: absolute; left: 0; right: 0; top: 362px; height: 56px;
    background: var(--paper);
    display: flex; align-items: center; padding-left: 40px;
    color: var(--forest); font-style: italic; font-weight: 700;
    font-size: 18px; letter-spacing: .5px; text-transform: uppercase;
    white-space: nowrap;
  }

  /* Contact side */
  .contact { background: var(--leaf); font-family: "Open Sans", Arial, sans-serif; }
  .contact__header {
    position: absolute; left: 0; right: 0; top: 0; height: 150px;
    background: var(--paper);
  }
  .contact__notch { position: absolute; left: 180px; top: 128px; }
  .contact__name {
    position: absolute; left: 60px; top: 62px;
    color: var(--forest); font-size: 40px; font-weight: 400; letter-spacing: .5px;
  }
  .brand {
    position: absolute; right: 44px; top: 40px;
    display: flex; align-items: center; gap: 10px;
  }
  .brand__dot { width: 30px; height: 30px; border-radius: 50%; background: var(--leaf); }
  .brand__name { color: var(--forest); font-size: 26px; font-weight: 600; line-height: 1.05; }
  .contact__details {
    position: absolute; left: 20px; width: 680px; top: 190px;
    text-align: center; color: var(--paper); font-style: normal;
    font-size: 20px; line-height: 38px; letter-spacing: .5px; text-transform: uppercase;
    white-space: nowrap;
  }
  .contact__web-band {
    position: absolute; left: 0; right: 0; top: 360px; height: 52px;
    background: var(--paper);
    display: flex; align-items: center; justify-content: flex-end; padding-right: 36px;
    color: var(--forest); font-size: 20px; font-weight: 600; letter-spacing: .4px;
  }
  .contact__base {
    position: absolute; left: 0; right: 0; bottom: 0; height: 30px; background: var(--paper);
  }
</style>
</head>
<body>
<main class="sheet">
  <section class="card appointment" aria-label="Appointment reminder side">
    <div class="appointment__fields">
      <div class="appointment__rule"></div>
      <div class="appointment__field"><span class="appointment__label">FOR</span><span class="appointment__line"></span></div>
      <div class="appointment__field"><span class="appointment__label">DATE</span><span class="appointment__line"></span></div>
      <div class="appointment__field"><span class="appointment__label">TIME</span><span class="appointment__line"></span></div>
    </div>
    <p class="appointment__notice">If you are unable to keep your appointment, kindly give 48 hours notice</p>
  </section>

  <section class="card contact" aria-label="Contact side">
    <div class="contact__header"></div>
    <svg class="contact__notch" width="60" height="24" viewBox="0 0 60 24" aria-hidden="true">
      <polygon points="0,24 18,2 42,2 60,24" fill="var(--leaf)"/>
    </svg>
    <h1 class="contact__name">Marlow T. Venn</h1>
    <div class="brand">
      <span class="brand__dot"></span>
      <span class="brand__name">Brightwave<br>Dental Care</span>
    </div>
    <address class="contact__details">
      DDS 2737 S. Fennimore Ave. Ste. 8 Royal Oak, MI 48059<br>
      Phone : (248)555-0174 | Fax : (248)555-0189<br>
      Email : info@BrightwaveDentalMi.example
    </address>
    <div class="contact__web-band">WWW.BRIGTHWAVEDENTALMI.EXAMPLE</div>
    <div class="contact__base"></div>
  </section>
</main>
</body>
</html>
```